Wordpress Design Project - Wedding Magazine Website

After looking at a few similar websites I formed a layout and colour scheme design in my head.
Then I came across this site (www.petalmarch.co.uk) which very close to what I am looking for in terms of layout of the page content and colours. So I would like something very similar but not so similar it just looks like a clone of this site. Almost identical in terms of how the content is laid out but colours and look and feel can be changed.
I have also provided a sketch of how I would like the content of the page to flow. See attachment.
Similar websites: in terms of content, style and layout.
http://www.lacebellmag.com/ (the colour scheme is good on this site. I also would like a similar background image as they have on their site.)
http://www.nuptivox.com/ (style and colour scheme is good on this site.)
of course you have the other sites i have reference in the initial tender.
Other general examples of wedding magazine style websites.
http://www.vowbrook.co.uk/
http://www.ringsandgarlands.co.uk/
http://www.thegoldenaisle.com/
http://www.veilor.com/
Style and layout: Wedding Theme
Colour Scheme: Clean and simple. White background in content area. Hints or highlights of grey/sliver, maybe pink here and there.
The page will flow as follows
Header part of the Page
- Name of the site on top left part of the page. “Tied by the Sea”.
- 728x90 horizontal banner aligned on right.
- Under the site name “Tied by the Sea” and banner will be a horizontal menu bar running the full width of the content
Main Content Area
- The main content column will be about 630px and the right sidebar will be about 330px. Similar width to most of the example URLs I have provided.
- Aligned to the left will be a slider
- Graphic or Pic: Guide to marrying in Spain: Everything you need to plan your wedding in spain.
- Graphic: Local Vendors Directory
- Articles 1 – 4
Right Sidebar (About 330px):
- Popular Post: Title of the Post and the first 2-3 lines of the post.
- 300x250 Ad Slot
- Locations: Title such as Barcelona then the first 2-3 lines of the post.
note: I haven't included a search box and login/register bits of content. i will leave it to you to figure out where these things will fit best on the page
=========================================================
Content of page
The horizontal menu bar: Home, Spanish Wedding Guide, Local Vendors Directory, Venues, Stag & Hen, Planning, Deals, Wedding Store.
For the wordpress theme the horizontal menubar will need to be a drop down menubar as we will have sub-menus for some of pages.
Images for slider
- Featured Venues
- Local vendors
- Deals
THE 2 COLUMN CONTENT AREA (Articles/Posts)
I am thinking that the first two bits of content in the 2 column area maybe should be graphics.
Spanish Wedding Guide -
Everything you need to plan your wedding in Spain.
Local Vendors Directory
(maybe this could be a graphic of a map of Spain)
=== from here you could use pictures or a mix of graphics and pictures to accompany each of these articles===
Front Page Main Content Articles
1. Legalities -
Want to tie the knot in Spain then you will find this post very useful.
2. Destination Barcelona -
Everything We LOVE About Barcelona!
3. Celebrity Weddings in Spain -
Find out who the latest celebrities to get married and Spain are and their chosen location.
4. Beach Weddings - With 4,964 km of coastline in Spain it is no surprise beach weddings are a popular choice.
under this will be the footer
Content we can populate later.
http://www.vowbrook.co.uk/
http://www.veilor.com/
Header part of the Page
- Under the site name “Tied by the Sea” will be a horizontal menu bar running the full width of the content
Main Content Area
- The main content column will be about 630px and the right sidebar will be about 330px. Similar width to most of the
example URLs I have provided.
Graphic or Pic: Guide to marrying in Spain: Everything you need to plan your wedding in spain.
Article 1 – 4
- 300x250 Ad Slot
note: i have left out a search bar and login area. I will leave that up to you. where you think they will fit on the page.
Content of page
Images for slider
- Featured Venues
- Local vendors
- Deals
Spanish Wedding Guide -
Local Vendors Directory
1. Legalities -
Please contact me for any questions. it maybe better to speak via skype or something.
Project Deadline Extended
Reason: It took me a few days to get acquainted with this site. As I don't have any designs in just yet I am extending the project a few days in order to give people time to submit their designs.
Something I would like to ad that i think designers will find useful.
The core of this site is the “Spanish Wedding Guide” and the “Local Vendor Directory”. These two things are what the site is all about so they need to feature. The viewers eyes must be drawn immediately to these two bit of information upon loading the page. These two things go underneath the slider.

```html
<!DOCTYPE html>
<html lang="en">
<head>
<meta charset="utf-8">
<title>Tied by the Sea</title>
<link href="https://fonts.googleapis.com/css2?family=Exo:wght@500&family=Gelasio:wght@400&family=Open+Sans:wght@400;600&family=Poiret+One&family=Ubuntu:wght@400&display=swap" rel="stylesheet">
<style>
:root{
  --page-bg:#f1dfbf;
  --page-bg-2:#e9d2ab;
  --sheet:#ffffff;
  --pink:#f676ac;
  --pink-light:#fba6cb;
  --pink-dark:#e9589a;
  --title-pink:#e8478d;
  --text:#6d6d6d;
  --text-dark:#333333;
  --muted:#a9a9a9;
  --rule:#d9d2c6;
  --frame:#e3dfd8;
  --panel:#fbf6ef;
  --panel-line:#eee4d5;
  --tab:#c7bda9;
  --footer-bg:#fdf9f4;
  --footer-head:#cf8c4e;
  --logo-grey:#6f6f6f;
}
*{box-sizing:border-box;margin:0;padding:0}
html,body{width:862px;height:1200px;overflow:hidden}
body{
  position:relative;
  background:radial-gradient(circle at 30% 20%,var(--page-bg) 0,var(--page-bg-2) 60%,var(--page-bg) 100%);
  font-family:"Open Sans",Tahoma,sans-serif;
  font-size:10px;color:var(--text);
}
.sheet{position:absolute;left:72px;top:5px;width:718px;height:1195px;background:var(--sheet)}
.abs{position:absolute}
a{color:inherit;text-decoration:none}

/* top bar */
.user-tab{left:420px;top:5px;width:172px;height:28px}
.user-tab span{position:absolute;left:27px;top:8px;font-size:9.5px;color:#fff}
.user-tab b{font-weight:400;color:var(--text-dark)}
.search-field{left:594px;top:11px;width:141px;height:20px;border:1px solid var(--rule);background:#fff;font-size:8.5px;color:#999;padding:4px 6px}
.search-btn{left:736px;top:11px;width:47px;height:20px;background:var(--pink);color:#fff;font-size:8.5px;text-align:center;line-height:20px}

/* header */
.site-name{left:79px;top:68px;font-family:"Exo",sans-serif;font-weight:500;font-size:22px;color:var(--logo-grey);letter-spacing:.3px}
.banner{left:260px;top:49px;width:523px;height:65px;background:#f8f4f0;border:1px solid #eee}
.banner-brand{position:absolute;left:0;top:0;width:185px;height:65px;background:var(--pink);color:#fff;font-family:"Ubuntu",sans-serif;font-size:29px;line-height:63px;text-align:center}
.banner-copy{position:absolute;left:205px;top:10px;font-family:"Poiret One",sans-serif;font-size:20px;line-height:22px;color:#777}
.banner-photo{position:absolute;right:0;top:0;width:95px;height:63px;background:linear-gradient(135deg,#e8e3de,#b9b3ac 60%,#f1ece6)}

/* nav */
.main-nav{left:79px;top:128px;width:704px;height:31px;background:linear-gradient(var(--pink-light),var(--pink) 55%,var(--pink-dark));border:1px solid #e35c97;display:flex}
.main-nav a{color:#fff;font-size:10px;line-height:29px;text-align:center;border-right:1px solid #f9b6d3}
.main-nav a.is-active{background:linear-gradient(#fcd0e3,#f8a6c9);color:var(--text-dark);font-weight:600}

/* slider */
.slider{left:79px;top:173px;width:453px;height:196px;border:4px solid #d0c8b7;background:linear-gradient(90deg,#d9c3a8 0,#eef2f4 45%,#e6eef2 100%)}
.slider-text{position:absolute;left:249px;top:33px;width:180px;font-size:9.5px;line-height:13px;color:#555}
.slider-dots{position:absolute;left:372px;top:164px;display:flex;gap:2px}
.slider-dots i{width:10px;height:10px;background:#c2bbaa}
.slider-dots i.on{background:var(--pink)}

/* posts */
.post-title{font-family:"Gelasio",Georgia,serif;font-size:13.5px;color:var(--title-pink);width:219px;padding-bottom:6px;border-bottom:1px solid var(--rule)}
.thumb{border:1px solid var(--frame);padding:3px;background:#fff}
.thumb div{width:100%;height:100%}
.excerpt{font-size:9.5px;line-height:13px;color:var(--text)}
.read-more{font-size:9px;color:var(--muted)}
.read-more::after{content:"";display:inline-block;margin-left:3px;border-left:3px solid var(--muted);border-top:3px solid transparent;border-bottom:3px solid transparent}

.section-bar{left:79px;top:538px;width:453px;height:29px;background:linear-gradient(var(--pink-light),var(--pink) 60%,var(--pink-dark));color:#fff;font-family:"Poiret One",sans-serif;font-size:19px;padding-left:11px;line-height:29px}

/* sidebar */
.widget{border:1px solid var(--panel-line);background:var(--panel)}
.widget-head{position:absolute;left:0;top:0;width:100%;height:32px;background:linear-gradient(var(--pink-light),var(--pink) 60%,var(--pink-dark));color:#fff;font-family:"Poiret One",sans-serif;font-size:19px;line-height:32px;padding-left:7px}
.widget-title{font-family:"Gelasio",Georgia,serif;font-size:11px;color:#6b5a40}
.ad-box{left:546px;top:383px;width:237px;height:201px;border:1px solid var(--panel-line);background:#fff}
.ad-art{position:absolute;left:10px;top:10px;width:216px;height:180px;background:radial-gradient(circle at 45% 40%,#f7c54d 0,#f3a85c 35%,#f9d9b8 80%)}
.ad-line{position:absolute;left:6px;top:129px;font-family:"Ubuntu",sans-serif;font-size:12.5px;color:#222}
.ad-brand{position:absolute;right:6px;top:150px;font-family:"Ubuntu",sans-serif;font-size:15px;color:#222}

/* footer */
.site-footer{left:72px;top:998px;width:718px;height:202px;background:var(--footer-bg);border-top:1px solid #f1ebe2}
.foot-col{position:absolute;top:25px}
.foot-col h4{font-family:"Gelasio",Georgia,serif;font-weight:400;font-size:11.5px;color:var(--footer-head);margin-bottom:10px}
.foot-col li{list-style:none;font-size:9.3px;line-height:15.8px;color:#666}
.foot-col p{font-size:9.3px;line-height:15.8px;color:#666;width:130px}
.social li{display:flex;align-items:center;gap:7px;height:27px}
.social i{display:block;width:20px;height:20px;border-radius:3px;background:#c9d3df}
.copyright{left:87px;top:1172px;width:689px;border-top:1px solid #eee5d9;padding-top:6px;text-align:center;font-size:9.3px;color:#666}
</style>
</head>
<body>
<div class="sheet"></div>

<svg class="abs user-tab" viewBox="0 0 172 28" aria-hidden="true"><path d="M0 28 C10 28 14 0 26 0 H172 V28Z" fill="#c7bda9"/></svg>
<div class="abs user-tab"><span>Welcome! (Log in) or <b>Register</b></span></div>
<div class="abs search-field">Enter Your Keyword...</div>
<div class="abs search-btn">SEARCH</div>

<header>
  <div class="abs site-name">Tied by the Sea</div>
  <div class="abs banner">
    <div class="banner-brand">Harrow Lane</div>
    <div class="banner-copy">View All Wedding Gift &amp;<br>Accessories</div>
    <div class="banner-photo" role="img" aria-label="Photo of a bride and groom in formal wear"></div>
  </div>
  <nav class="abs main-nav">
    <a class="is-active" style="width:52px">Home</a>
    <a style="width:134px">Spanish Wedding Guide</a>
    <a style="width:134px">Local Vendors Directory</a>
    <a style="width:60px">Venues</a>
    <a style="width:78px">Stag &amp; Hen</a>
    <a style="width:66px">Planning</a>
    <a style="width:52px">Deals</a>
    <a style="width:110px;border-right:0">Wedding Store</a>
  </nav>
</header>

<main>
  <div class="abs slider" role="img" aria-label="Slider photo of a smiling couple on a beach">
    <p class="slider-text">Lorem Ipsum is simply dummy text of the printing and typesetting industry. Lorem Ipsum has been the industry's standard dummy text ever since the 1500s, when an unknown printer took a galley of type and scrambled it to make a type specimen book.</p>
    <div class="slider-dots"><i class="on"></i><i></i><i></i><i></i><i></i></div>
  </div>

  <h3 class="abs post-title" style="left:79px;top:388px">Spanish Wedding Guide</h3>
  <div class="abs thumb" style="left:86px;top:418px;width:88px;height:105px"><div role="img" aria-label="Photo of a bride" style="background:linear-gradient(135deg,#c9783f,#f0c9a5 50%,#b8885c)"></div></div>
  <p class="abs excerpt" style="left:181px;top:415px;width:110px">Everything you need to plan your wedding in Spain.</p>
  <span class="abs read-more" style="left:241px;top:509px">Read More</span>

  <h3 class="abs post-title" style="left:312px;top:388px">Local Vendors Directory</h3>
  <div class="abs thumb" style="left:319px;top:418px;width:88px;height:105px"><div role="img" aria-label="Photo of blue place cards on a table" style="background:linear-gradient(160deg,#f4f4f4 0,#4fb3e6 45%,#1b1b1b 90%)"></div></div>
  <p class="abs excerpt" style="left:414px;top:415px;width:112px">Lorem Ipsum is simply dummy text the printing and typesetting industry. Lorem Ipsum has been the industry's standard dummy text ever dummy since the 1500s...</p>
  <span class="abs read-more" style="left:474px;top:509px">Read More</span>

  <div class="abs section-bar">Articles</div>

  <h3 class="abs post-title" style="left:79px;top:586px">Legalities</h3>
  <div class="abs thumb" style="left:86px;top:615px;width:205px;height:96px"><div role="img" aria-label="Photo of a couple at a registry office" style="background:linear-gradient(90deg,#5a3b2c,#b08c70 50%,#4b3a33)"></div></div>
  <p class="abs excerpt" style="left:87px;top:715px;width:215px">Want to tie the knot in Spain then you will find this post very useful.</p>
  <span class="abs read-more" style="left:241px;top:753px">Read More</span>

  <h3 class="abs post-title" style="left:312px;top:586px">Destination Barcelona</h3>
  <div class="abs thumb" style="left:319px;top:615px;width:205px;height:96px"><div role="img" aria-label="Photo of a bride and groom outdoors" style="background:linear-gradient(90deg,#2f4a2a,#9aa88a 50%,#3c5631)"></div></div>
  <p class="abs excerpt" style="left:320px;top:715px;width:215px">Everything We LOVE About Barcelona!</p>
  <span class="abs read-more" style="left:474px;top:753px">Read More</span>

  <h3 class="abs post-title" style="left:79px;top:781px">Celebrity Weddings in Spain</h3>
  <div class="abs thumb" style="left:86px;top:810px;width:205px;height:96px"><div role="img" aria-label="Photo of a smiling bride and groom" style="background:linear-gradient(90deg,#e8e6c8,#d9bfa5 50%,#6e7a4a)"></div></div>
  <p class="abs excerpt" style="left:87px;top:911px;width:215px">Find out who the latest celebrities to get married and Spain are and their chosen location.</p>
  <span class="abs read-more" style="left:241px;top:948px">Read More</span>

  <h3 class="abs post-title" style="left:312px;top:781px">Beach Weddings</h3>
  <div class="abs thumb" style="left:319px;top:810px;width:205px;height:96px"><div role="img" aria-label="Photo of a couple on the beach" style="background:linear-gradient(90deg,#c9d6dc,#e9e2d6 50%,#a99a8c)"></div></div>
  <p class="abs excerpt" style="left:320px;top:911px;width:215px">With 4,964 km of coastline in Spain it is no surprise beach weddings are a popular choice.</p>
  <span class="abs read-more" style="left:474px;top:948px">Read More</span>
</main>

<aside>
  <section class="abs widget" style="left:546px;top:173px;width:237px;height:196px">
    <h3 class="widget-head">Popular Posts</h3>
    <div class="abs thumb" style="left:8px;top:40px;width:86px;height:104px"><div role="img" aria-label="Photo of pink wedding accessories" style="background:linear-gradient(135deg,#f7d8e4,#f3a9c6 60%,#fbeef2)"></div></div>
    <h4 class="abs widget-title" style="left:101px;top:36px">Wedding Accessories</h4>
    <p class="abs excerpt" style="left:101px;top:55px;width:126px">Lorem Ipsum is simply dummy text of the printing and typesetting industry, Lorem Ipsum has been the dummy industry's since the 1500s...</p>
    <span class="abs read-more" style="left:179px;top:148px">Read More</span>
  </section>

  <div class="abs ad-box">
    <div class="ad-art" role="img" aria-label="Illustration of two gold wedding rings on a peach background">
      <span class="ad-line">Celebrate Your Wedding Gift List</span>
      <span class="ad-brand">Harrow Lane</span>
    </div>
  </div>

  <section class="abs widget" style="left:546px;top:598px;width:237px;height:160px">
    <h3 class="widget-head">Location</h3>
    <div class="abs thumb" style="left:8px;top:40px;width:86px;height:103px"><div role="img" aria-label="Photo of a tower and fountain in Barcelona" style="background:linear-gradient(#4b8fd6,#a8c7e3 50%,#8a8c6a)"></div></div>
    <h4 class="abs widget-title" style="left:101px;top:36px">Barcelona Wedding</h4>
    <p class="abs excerpt" style="left:101px;top:55px;width:126px">Lorem Ipsum is simply dummy text of the printing Lorem Ipsum has been the industry's standard dummy text ever since the 1500s.</p>
    <span class="abs read-more" style="left:179px;top:122px">Read More</span>
  </section>
</aside>

<footer class="abs site-footer">
  <div class="foot-col" style="left:15px">
    <h4>Quick Links</h4>
    <ul><li>Home</li><li>Spanish Wedding Guide Local</li><li>Vendors Directory Venues</li><li>Stag &amp; Hen</li><li>Planning</li><li>Deals</li><li>Wedding Store</li></ul>
  </div>
  <div class="foot-col" style="left:202px">
    <h4>Articals</h4>
    <ul><li>Legalities</li><li>Destination Barcelona</li><li>Celebrity Weddings in Spain</li><li>Beach Weddings</li></ul>
  </div>
  <div class="foot-col" style="left:384px">
    <h4>Contact Us</h4>
    <p>Lorem Ipsum is simply dummy text of the printing and type-setting industry. Lorem Ipsum has been the industry's stan-dard dummy text ever since the 1500s...</p>
  </div>
  <div class="foot-col social" style="left:577px">
    <h4>Follow Us On</h4>
    <ul><li><i></i>Follow us on Friendspace</li><li><i></i>Follow us on Chirpline</li><li><i></i>Follow us on Workmesh</li></ul>
  </div>
</footer>
<div class="abs copyright">Copyright© 2012 Tied by the Sea. All Right Reserved.</div>
</body>
</html>
```